Brambleton Resource Holdings, LP Letter Head

We need an official company letter head design that is clean and mimics our company logo style. It will include our logo, address, phone, and website. We are an OIl and Gas mineral purchasing company, so hints of oil rigs or related design would be desirable.

Industry/Entity Type

Oil And Gas

Colors
ec1f27
f04a50
f59195
fbd4d5

Requirements
Must have
• Logo
• 7392 Whitcombe R. Ashdale Parkway, Suite 618
• Dallas TX, 75391
• 214-673-1958
• www.bramblestoneres.example
Nice to have
• Oil Rigs or OIl and gas related design

```html
<!DOCTYPE html>
<html lang="en">
<head>
<meta charset="utf-8">
<title>Brambleton Resource Holdings – Letterhead</title>
<link rel="stylesheet" href="https://fonts.googleapis.com/css2?family=Cinzel:wght@500&family=Roboto:wght@400&display=swap">
<style>
  :root {
    --backdrop: #e6e6e6;
    --paper: #f5f5f5;
    --brand-red: #c3161f;
    --mark-tint: #ece9e9;
    --mark-line: #eeecec;
    --ink: #2b2b2b;
    --rule: #9a9a9a;
  }
  html, body {
    margin: 0;
    padding: 0;
    width: 1200px;
    height: 734px;
    overflow: hidden;
    background: var(--backdrop);
  }
  .canvas {
    position: relative;
    width: 1200px;
    height: 734px;
  }
  .letterhead {
    position: absolute;
    left: 353px;
    top: 17px;
    width: 494px;
    height: 700px;
    background: var(--paper);
    box-shadow: 0 1px 3px rgba(0,0,0,0.12);
  }
  .brand {
    position: absolute;
    top: 34px;
    left: 0;
    width: 100%;
    text-align: center;
  }
  .brand-square {
    display: block;
    width: 54px;
    height: 54px;
    margin: 0 auto 10px;
    background: var(--brand-red);
  }
  .brand-name {
    margin: 0;
    font-family: 'Cinzel', serif;
    font-weight: 500;
    font-size: 16px;
    line-height: 17px;
    letter-spacing: 1.5px;
    color: var(--brand-red);
  }
  .backdrop-mark {
    position: absolute;
    left: 113px;
    top: 251px;
    width: 272px;
    height: 275px;
    box-sizing: border-box;
    border: 8px solid var(--mark-line);
    padding: 10px;
  }
  .backdrop-mark-fill {
    width: 100%;
    height: 100%;
    background: var(--mark-tint);
  }
  .contact-bar {
    position: absolute;
    left: 0;
    top: 662px;
    width: 100%;
    display: flex;
    justify-content: center;
    align-items: center;
    font-family: 'Roboto', sans-serif;
    font-size: 7.6px;
    color: var(--ink);
    white-space: nowrap;
  }
  .contact-item {
    display: flex;
    align-items: center;
    gap: 4px;
  }
  .contact-divider {
    width: 1px;
    height: 15px;
    background: var(--rule);
    margin: 0 11px;
  }
  .contact-icon {
    width: 8px;
    height: 8px;
  }
</style>
</head>
<body>
<div class="canvas">
  <section class="letterhead" aria-label="Brambleton Resource Holdings letterhead">
    <header class="brand">
      <span class="brand-square"></span>
      <p class="brand-name">Brambleton<br>Resource Holdings</p>
    </header>

    <div class="backdrop-mark" aria-hidden="true">
      <div class="backdrop-mark-fill"></div>
    </div>

    <footer class="contact-bar">
      <span class="contact-item">7392 Whitcombe R. Ashdale Parkway, Suite 618, Dallas TX, 75391</span>
      <span class="contact-divider"></span>
      <span class="contact-item">
        <svg class="contact-icon" viewBox="0 0 16 16" aria-hidden="true">
          <path d="M3.5 1.5l2.5 0 1.2 3.2-1.6 1.2c0.8 1.8 2.2 3.2 4 4l1.2-1.6 3.2 1.2 0 2.5c0 0.8-0.7 1.5-1.5 1.5C6.7 13.5 2.5 9.3 2 3c0-0.8 0.7-1.5 1.5-1.5z" fill="#c3161f"/>
        </svg>
        214-673-1958
      </span>
      <span class="contact-divider"></span>
      <span class="contact-item">
        <svg class="contact-icon" viewBox="0 0 16 16" aria-hidden="true">
          <rect x="1.5" y="3.5" width="13" height="9" fill="none" stroke="#c3161f" stroke-width="1.5"/>
          <path d="M1.5 3.5l6.5 5 6.5-5" fill="none" stroke="#c3161f" stroke-width="1.5"/>
        </svg>
        www.bramblestoneres.example
      </span>
    </footer>
  </section>
</div>
</body>
</html>
```